Designing a website for Brightmoor Pest Services PTY LTD

Pest control company looking for someone to build an informative website containing services we offer and an online inquiry form.
Commercial premises - Specialising in - Rodent control, stored product pest control, flying insect control, ant, spider and insect control, Termite inspections and treatments. Termite management systems on a commercial scale.
Facilities we service
Commercial - shopping centres, transport facilities, restaurants, pubs, clubs, bars food manufacturing facilities.
Residential - Houses specialising in - Rodent, Ant, Spider, Cockroach and Termite control. Termite inspections, Pre - purchase inspections, Termite treatments, Termite management systems.
Target Market(s)
Mainly commercial and industrial clients and Residential clients.
Industry/Entity Type
Pest Control
Number of Pages Required
1 page
Look and feel

```html
<!DOCTYPE html>
<html lang="en">
<head>
<meta charset="utf-8">
<title>Brightmoor Pest Services PTY LTD</title>
<link href="https://fonts.googleapis.com/css2?family=Exo+2:wght@400;500;600&family=Montserrat:wght@400;500;600;700&family=Rajdhani:wght@500;600&display=swap" rel="stylesheet">
<style>
:root{
  --green:#3a9a0a;
  --green-dark:#2e8606;
  --ink:#1e1e1e;
  --text:#555;
  --muted:#8a8a8a;
  --footer:#1d1d1d;
  --white:#fff;
  --header:#f3f3f3;
  --pale:#e9eee6;
  --icon:#2b2b2b;
}
*{box-sizing:border-box;margin:0;padding:0}
html,body{width:1200px;height:3968px;overflow:hidden}
body{position:relative;background:var(--white);font-family:"Montserrat",sans-serif;color:var(--text)}
.abs{position:absolute}
.btn{position:absolute;display:flex;align-items:center;justify-content:center;font-family:"Montserrat",sans-serif;font-weight:700;font-size:13px;text-transform:uppercase;color:var(--white);border-radius:3px}
.btn-green{background:var(--green)}
.btn-black{background:#0d0d0d}

/* header */
.site-header{left:0;top:0;width:1200px;height:82px;background:var(--header)}
.brand{font-family:"Exo 2",sans-serif;font-weight:600;font-size:22px;color:var(--ink);display:flex;align-items:center;gap:10px;white-space:nowrap}
.brand-dot{width:14px;height:14px;border-radius:50%;background:var(--green)}
.nav{font-size:11px;text-transform:uppercase;color:#9a9a9a}
.nav a{position:absolute;white-space:nowrap;text-decoration:none;color:inherit}
.nav .active{color:var(--green)}

/* hero */
.hero-photo{left:0;top:82px;width:1200px;height:600px;background:
  radial-gradient(ellipse 180px 260px at 520px 380px,rgba(214,180,40,.55),transparent 70%),
  radial-gradient(ellipse 420px 300px at 880px 260px,rgba(235,235,235,.55),transparent 70%),
  linear-gradient(120deg,#4c3a30 0%,#8a7a70 35%,#6e6660 60%,#3c3835 100%)}
.hero-box{left:293px;top:249px;width:614px;height:244px;background:rgba(40,40,40,.72)}
.hero-title{left:293px;top:268px;width:614px;text-align:center;font-family:"Rajdhani",sans-serif;font-weight:600;font-size:48px;line-height:60px;color:var(--white)}

/* about */
.section-title{font-family:"Exo 2",sans-serif;font-weight:500;color:var(--ink)}
.about-para{left:627px;top:840px;width:370px;font-size:12px;line-height:20px;color:var(--muted)}
.ticks{left:627px;top:913px;list-style:none;font-size:12px;color:var(--muted)}
.ticks li{position:absolute;left:0;white-space:nowrap;display:flex;align-items:center;gap:18px}

/* commercial premises */
.premises-photo{left:0;top:1178px;width:1200px;height:505px;background:
  radial-gradient(ellipse 260px 320px at 620px 360px,rgba(20,20,20,.55),transparent 70%),
  radial-gradient(ellipse 300px 200px at 150px 320px,rgba(110,100,90,.5),transparent 70%),
  linear-gradient(110deg,#3d3f41 0%,#2b2d2f 45%,#4b4d4e 100%)}
.premise{position:absolute;width:150px;text-align:center;color:var(--white);font-size:14px;line-height:18px;font-family:"Exo 2",sans-serif}
.premise .ring{width:78px;height:78px;border-radius:50%;margin:0 auto 14px;background:rgba(255,255,255,.25);display:flex;align-items:center;justify-content:center;color:var(--white)}
.premise.featured .ring{background:var(--white);border:3px solid var(--green);color:var(--green)}
.premise .ring svg{width:40px;height:40px}

/* contact band */
.contact-band{left:0;top:1683px;width:1200px;height:300px;background:linear-gradient(90deg,#dfe6da,#eef2ea)}
.contact-call{left:102px;top:1775px;font-family:"Rajdhani",sans-serif;font-weight:600;font-size:32px;line-height:45px;color:var(--ink);text-transform:uppercase}
.phone-line{left:102px;top:1883px;display:flex;align-items:center;gap:12px;font-family:"Rajdhani",sans-serif;font-weight:600;font-size:24px;color:var(--green)}
.form-panel{left:614px;top:1785px;width:526px;height:449px;background:var(--green)}
.form-title{left:664px;top:1826px;font-family:"Rajdhani",sans-serif;font-weight:600;font-size:32px;color:var(--white)}
.field{position:absolute;background:rgba(255,255,255,.18);border-radius:2px;color:var(--white);font-size:11px;padding:10px 16px}

/* service cards */
.card{background:var(--white);box-shadow:0 0 18px rgba(0,0,0,.12)}
.svc{position:absolute;display:flex;align-items:center;gap:20px;font-size:13px;font-weight:600;color:var(--ink);line-height:17px}
.svc .ico{position:relative;width:48px;height:42px;flex:none;color:var(--icon)}
.svc .ico::before{content:"";position:absolute;left:0;top:6px;width:32px;height:32px;border-radius:50%;background:#e7efe2}
.svc .ico svg{position:absolute;left:6px;top:2px;width:38px;height:38px}

/* cta */
.cta-band{left:0;top:3285px;width:1200px;height:329px}
.cta-text{left:0;top:3398px;width:1200px;text-align:center;font-family:"Exo 2",sans-serif;font-size:24px;line-height:31px;color:var(--white)}
.btn-outline{border:2px solid var(--white);border-radius:20px;background:transparent}
.btn-pill{border-radius:20px}

/* footer */
.site-footer{left:0;top:3614px;width:1200px;height:302px;background:var(--footer)}
.foot-title{font-family:"Exo 2",sans-serif;font-weight:400;font-size:20px;color:var(--white)}
.foot-link{font-size:12px;color:#dcdcdc}
.social{width:32px;height:32px;border:2px solid var(--green);border-radius:50%}
.copyright{left:0;top:3916px;width:1200px;height:52px;background:var(--green);color:var(--white);font-size:12px;display:flex;align-items:center;justify-content:center}
</style>
</head>
<body>

<svg width="0" height="0" style="position:absolute" aria-hidden="true">
  <defs>
    <symbol id="i-shield" viewBox="0 0 40 40"><path d="M20 4 33 9v10c0 8-6 14-13 17C13 33 7 27 7 19V9z" fill="none" stroke="currentColor" stroke-width="2.2" stroke-linejoin="round"/><path d="M14 20l4.5 4.5L27 15" fill="none" stroke="currentColor" stroke-width="2.4" stroke-linecap="round" stroke-linejoin="round"/></symbol>
    <symbol id="i-box" viewBox="0 0 40 40"><path d="M20 5 34 12v16L20 35 6 28V12z M6 12l14 7 14-7 M20 19v16" fill="none" stroke="currentColor" stroke-width="2.2" stroke-linejoin="round"/></symbol>
    <symbol id="i-target" viewBox="0 0 40 40"><circle cx="20" cy="20" r="12" fill="none" stroke="currentColor" stroke-width="2.2"/><circle cx="20" cy="20" r="4" fill="currentColor"/><path d="M20 3v8 M20 29v8 M3 20h8 M29 20h8" stroke="currentColor" stroke-width="2.2" stroke-linecap="round"/></symbol>
    <symbol id="i-dots" viewBox="0 0 40 40"><circle cx="20" cy="20" r="14" fill="none" stroke="currentColor" stroke-width="2.2"/><circle cx="14" cy="16" r="2.6" fill="currentColor"/><circle cx="26" cy="16" r="2.6" fill="currentColor"/><circle cx="20" cy="26" r="2.6" fill="currentColor"/><path d="M9 9 31 31" stroke="currentColor" stroke-width="2.2" stroke-linecap="round"/></symbol>
    <symbol id="i-web" viewBox="0 0 40 40"><path d="M20 4 34 12v16L20 36 6 28V12z M20 11l8 4.5v9L20 29l-8-4.5v-9z M20 4v32 M6 12l28 16 M34 12 6 28" fill="none" stroke="currentColor" stroke-width="1.9" stroke-linejoin="round"/></symbol>
    <symbol id="i-search" viewBox="0 0 40 40"><circle cx="17" cy="17" r="10" fill="none" stroke="currentColor" stroke-width="2.4"/><path d="M24.5 24.5 34 34" stroke="currentColor" stroke-width="3" stroke-linecap="round"/></symbol>
    <symbol id="i-glass" viewBox="0 0 40 40"><path d="M11 6h18l-3 28H14z M12 13h16" fill="none" stroke="currentColor" stroke-width="2.2" stroke-linejoin="round"/><path d="M29 14h3a3 3 0 0 1 3 3v5a3 3 0 0 1-3 3h-3.8" fill="none" stroke="currentColor" stroke-width="2.2"/></symbol>
    <symbol id="i-truck" viewBox="0 0 40 40"><rect x="4" y="11" width="32" height="16" rx="4" fill="none" stroke="currentColor" stroke-width="2.2"/><path d="M9 15h6v5H9z M17 15h6v5h-6z M25 15h6v5h-6z" fill="none" stroke="currentColor" stroke-width="1.8"/><circle cx="11" cy="30" r="3" fill="none" stroke="currentColor" stroke-width="2"/><circle cx="29" cy="30" r="3" fill="none" stroke="currentColor" stroke-width="2"/></symbol>
    <symbol id="i-disc" viewBox="0 0 40 40"><rect x="5" y="7" width="30" height="26" rx="4" fill="none" stroke="currentColor" stroke-width="2.2"/><circle cx="20" cy="20" r="8" fill="none" stroke="currentColor" stroke-width="2.2"/><circle cx="20" cy="20" r="2.5" fill="currentColor"/></symbol>
    <symbol id="i-building" viewBox="0 0 40 40"><path d="M6 35h28 M9 35V12h22v23 M9 12l11-7 11 7" fill="none" stroke="currentColor" stroke-width="2.2" stroke-linejoin="round"/><path d="M13 17h4v4h-4z M23 17h4v4h-4z M17 27h6v8h-6z" fill="none" stroke="currentColor" stroke-width="1.8"/></symbol>
    <symbol id="i-factory" viewBox="0 0 40 40"><path d="M5 35V18l9 5v-5l9 5v-5l9 5V7h4v28z" fill="none" stroke="currentColor" stroke-width="2.2" stroke-linejoin="round"/><path d="M10 28h4 M18 28h4 M26 28h4" stroke="currentColor" stroke-width="2.2"/></symbol>
    <symbol id="i-home" viewBox="0 0 40 40"><path d="M5 19 20 6l15 13 M9 16v18h22V16" fill="none" stroke="currentColor" stroke-width="2.2" stroke-linejoin="round"/><path d="M17 34v-9h6v9" fill="none" stroke="currentColor" stroke-width="2"/></symbol>
  </defs>
</svg>

<header class="abs site-header">
  <div class="abs brand" style="left:58px;top:27px"><span class="brand-dot"></span>Brightmoor Pest Services</div>
  <nav class="abs nav" style="left:0;top:31px;width:1200px">
    <svg class="abs" style="left:606px;top:-2px" width="18" height="16" viewBox="0 0 18 16"><path d="M9 1 1 8h2.5v7h4v-4.5h3V15h4V8H17z" fill="#3a9a0a"/></svg>
    <a class="active" style="left:642px">Home</a>
    <a style="left:710px">Services</a>
    <a style="left:799px">About Us</a>
    <a style="left:890px">Contact Us</a>
  </nav>
  <div class="btn btn-green" style="left:998px;top:24px;width:142px;height:35px">Online Inquiry</div>
</header>

<section>
  <div class="abs hero-photo" role="img" aria-label="Technician in protective suit spraying pest treatment along a skirting board"></div>
  <div class="abs hero-box"></div>
  <h1 class="abs hero-title">WE CARE ABOUT<br>YOUR PEST INFESTATION</h1>
  <div class="btn btn-green" style="left:453px;top:422px;width:123px;height:35px">Contact Us</div>
  <div class="btn btn-black" style="left:602px;top:422px;width:143px;height:35px">Online Inquiry</div>
  <svg class="abs" style="left:0;top:500px" width="1200" height="190" viewBox="0 0 1200 190">
    <path d="M0 16 C180 110 360 178 620 170 C850 162 1040 120 1200 100 V190 H0Z" fill="#fff"/>
    <path d="M560 170 C800 168 1020 126 1200 96 V120 C1020 140 820 176 620 176 Z" fill="#3a9a0a"/>
  </svg>
</section>

<section>
  <svg class="abs" style="left:120px;top:740px" width="400" height="380" viewBox="0 0 400 380">
    <circle cx="22" cy="56" r="5" fill="#111"/><circle cx="40" cy="52" r="8" fill="#111"/><circle cx="68" cy="46" r="12" fill="#111"/>
    <circle cx="228" cy="22" r="10" fill="#3a9a0a"/><circle cx="206" cy="34" r="5" fill="#3a9a0a"/>
    <circle cx="113" cy="215" r="150" fill="#2f8a08"/>
    <circle cx="277" cy="145" r="102" fill="#111"/>
    <circle cx="387" cy="228" r="12" fill="#3a9a0a"/><circle cx="363" cy="244" r="7" fill="#3a9a0a"/><circle cx="344" cy="256" r="4" fill="#3a9a0a"/>
    <circle cx="278" cy="283" r="11" fill="#111"/><circle cx="268" cy="308" r="6" fill="#111"/>
  </svg>
  <div class="abs" style="left:105px;top:831px;width:250px;height:250px;border-radius:50%;background:radial-gradient(circle at 40% 30%,#f1e4cc,#c9b596 45%,#8a9b5a 85%)" role="img" aria-label="Inspector with a clipboard and hard hat examining the base of a house wall"></div>
  <div class="abs" style="left:312px;top:802px;width:170px;height:170px;border-radius:50%;background:radial-gradient(circle at 65% 35%,#f2f3f5,#b8c1cf 45%,#2f4f8a 90%)" role="img" aria-label="Pest technician in uniform talking with a homeowner in a kitchen"></div>

  <svg class="abs" style="left:624px;top:758px" width="62" height="70" viewBox="0 0 62 70"><path d="M58 6 C30 -4 4 14 4 40 C4 52 10 62 18 66" fill="none" stroke="#dfe8d8" stroke-width="6"/></svg>
  <h2 class="abs section-title" style="left:657px;top:776px;font-size:30px">About Us</h2>
  <p class="abs about-para">Lorem ipsum is simply dummy text of the printing and typesetting industry. Lorem Ipsum has been the industry's standard dummy text ever since the 1500s,</p>
  <ul class="abs ticks">
    <li style="top:0"><svg width="16" height="16" viewBox="0 0 16 16"><circle cx="8" cy="8" r="6.5" fill="none" stroke="#3a9a0a" stroke-width="1.6"/><path d="M4.5 8 7 10.5 13 3.5" fill="none" stroke="#111" stroke-width="2"/></svg>There are many variations of passages</li>
    <li style="top:37px"><svg width="16" height="16" viewBox="0 0 16 16"><circle cx="8" cy="8" r="6.5" fill="none" stroke="#3a9a0a" stroke-width="1.6"/><path d="M4.5 8 7 10.5 13 3.5" fill="none" stroke="#111" stroke-width="2"/></svg>which don't look even slightly believable</li>
    <li style="top:75px"><svg width="16" height="16" viewBox="0 0 16 16"><circle cx="8" cy="8" r="6.5" fill="none" stroke="#3a9a0a" stroke-width="1.6"/><path d="M4.5 8 7 10.5 13 3.5" fill="none" stroke="#111" stroke-width="2"/></svg>making this the first true generator on the Internet</li>
    <li style="top:112px"><svg width="16" height="16" viewBox="0 0 16 16"><circle cx="8" cy="8" r="6.5" fill="none" stroke="#3a9a0a" stroke-width="1.6"/><path d="M4.5 8 7 10.5 13 3.5" fill="none" stroke="#111" stroke-width="2"/></svg>The generated Lorem Ipsum</li>
  </ul>
  <div class="btn btn-green" style="left:627px;top:1066px;width:151px;height:37px;border-radius:19px;font-size:15px">View More</div>
</section>

<section>
  <div class="abs premises-photo" role="img" aria-label="Technician in a respirator spraying treatment outside a commercial building"></div>
  <svg class="abs" style="left:0;top:1170px" width="1200" height="170" viewBox="0 0 1200 170">
    <path d="M0 0 H1200 V165 C1000 60 760 30 560 30 C330 30 150 58 0 90Z" fill="#fff"/>
    <path d="M0 64 C180 36 360 10 580 10 C800 10 1000 50 1200 140 V165 C1000 60 780 28 560 28 C330 28 150 56 0 90Z" fill="#3a9a0a"/>
  </svg>
  <h2 class="abs" style="left:0;top:1276px;width:1200px;text-align:center;font-family:'Exo 2',sans-serif;font-weight:500;font-size:32px;color:#fff">Commercial premises</h2>
  <div class="premise featured" style="left:131px;top:1351px"><div class="ring"><svg aria-hidden="true"><use href="#i-shield"/></svg></div>Rodent control</div>
  <div class="premise" style="left:292px;top:1351px"><div class="ring"><svg aria-hidden="true"><use href="#i-box"/></svg></div>stored product<br>pest</div>
  <div class="premise" style="left:452px;top:1351px"><div class="ring"><svg aria-hidden="true"><use href="#i-target"/></svg></div>flying insect<br>control</div>
  <div class="premise" style="left:604px;top:1351px"><div class="ring"><svg aria-hidden="true"><use href="#i-dots"/></svg></div>ant</div>
  <div class="premise" style="left:754px;top:1351px"><div class="ring"><svg aria-hidden="true"><use href="#i-web"/></svg></div><span style="position:relative;top:-8px">spider and insect<br>control</span></div>
  <div class="premise" style="left:904px;top:1351px"><div class="ring"><svg aria-hidden="true"><use href="#i-search"/></svg></div><span style="position:relative;top:-12px">Termite<br>inspections</span></div>
  <div class="btn btn-green" style="left:537px;top:1537px;width:124px;height:35px">View More</div>
</section>

<section>
  <div class="abs contact-band"></div>
  <h2 class="abs contact-call">Don't hesitate to<br>contact us any time.</h2>
  <div class="abs phone-line"><svg width="22" height="22" viewBox="0 0 24 24"><path d="M6.6 10.8c1.4 2.8 3.8 5.1 6.6 6.6l2.2-2.2c.3-.3.7-.4 1-.2 1.1.4 2.3.6 3.6.6.6 0 1 .4 1 1V20c0 .6-.4 1-1 1C10.6 21 3 13.4 3 4c0-.6.4-1 1-1h3.5c.6 0 1 .4 1 1 0 1.3.2 2.5.6 3.6.1.3 0 .7-.2 1z" fill="#3a9a0a"/></svg>+61 2 5550 0137</div>

  <div class="abs form-panel"></div>
  <svg class="abs" style="left:632px;top:1810px" width="60" height="66" viewBox="0 0 60 66"><path d="M56 6 C30 -4 4 12 4 36 C4 48 10 58 18 62" fill="none" stroke="rgba(255,255,255,.25)" stroke-width="5"/></svg>
  <h2 class="abs form-title">CONTACT US</h2>
  <div class="field" style="left:645px;top:1919px;width:224px;height:35px">Name:</div>
  <div class="field" style="left:885px;top:1919px;width:224px;height:35px">Email :</div>
  <div class="field" style="left:645px;top:1971px;width:224px;height:36px">Phone :</div>
  <div class="field" style="left:885px;top:1971px;width:224px;height:36px">Subject :</div>
  <div class="field" style="left:645px;top:2025px;width:464px;height:65px">Message :</div>
  <div class="btn btn-black" style="left:654px;top:2110px;width:134px;height:35px;font-size:12px">Submit Now</div>
</section>

<section>
  <svg class="abs" style="left:242px;top:2205px" width="266" height="305" viewBox="0 0 266 305"><path d="M0 0 H212 L266 60 V305 H0Z" fill="#3a9a0a"/></svg>
  <div class="abs" style="left:290px;top:2305px;width:146px;height:239px;background:linear-gradient(90deg,#eef0ee 0%,#dcdcd8 45%,#a27d5e 70%,#6b4c36 100%)" role="img" aria-label="Technician spraying treatment under a kitchen sink"></div>
  <div class="abs card" style="left:434px;top:2288px;width:525px;height:376px"></div>
  <h2 class="abs section-title" style="left:488px;top:2352px;font-size:28px">Commercial Services</h2>
  <div class="svc" style="left:488px;top:2413px"><span class="ico"><svg aria-hidden="true"><use href="#i-shield"/></svg></span>Rodent control</div>
  <div class="svc" style="left:745px;top:2413px"><span class="ico"><svg aria-hidden="true"><use href="#i-glass"/></svg></span>Pubs</div>
  <div class="svc" style="left:488px;top:2495px"><span class="ico"><svg aria-hidden="true"><use href="#i-truck"/></svg></span>Transport facilities</div>
  <div class="svc" style="left:745px;top:2495px"><span class="ico"><svg aria-hidden="true"><use href="#i-disc"/></svg></span>Clubs</div>
  <div class="svc" style="left:488px;top:2589px"><span class="ico"><svg aria-hidden="true"><use href="#i-building"/></svg></span>Restaurants</div>
  <div class="svc" style="left:745px;top:2589px"><span class="ico"><svg aria-hidden="true"><use href="#i-factory"/></svg></span>Bars food<br>manufacturing</div>
</section>

<section>
  <div class="abs" style="left:662px;top:2746px;width:293px;height:349px;background:radial-gradient(ellipse 120px 170px at 190px 170px,#f6f7f8,transparent 75%),linear-gradient(135deg,#b9bec6,#e4e7ea 45%,#6f7985)" role="img" aria-label="Technician in a white protective suit spraying inside a home"></div>
  <svg class="abs" style="left:880px;top:3030px" width="80" height="80" viewBox="0 0 80 80"><path d="M80 0 V80 H0Z" fill="#3a9a0a"/></svg>
  <div class="abs card" style="left:254px;top:2858px;width:525px;height:373px"></div>
  <h2 class="abs section-title" style="left:308px;top:2922px;font-size:28px">Residential Services</h2>
  <div class="svc" style="left:308px;top:2981px"><span class="ico"><svg aria-hidden="true"><use href="#i-shield"/></svg></span>Rodent</div>
  <div class="svc" style="left:565px;top:2981px"><span class="ico"><svg aria-hidden="true"><use href="#i-search"/></svg></span>Termite<br>inspections</div>
  <div class="svc" style="left:308px;top:3063px"><span class="ico"><svg aria-hidden="true"><use href="#i-dots"/></svg></span>Ant</div>
  <div class="svc" style="left:565px;top:3063px"><span class="ico"><svg aria-hidden="true"><use href="#i-home"/></svg></span>Termite control</div>
  <div class="svc" style="left:308px;top:3157px"><span class="ico"><svg aria-hidden="true"><use href="#i-web"/></svg></span>Spider</div>
  <div class="svc" style="left:565px;top:3157px"><span class="ico"><svg aria-hidden="true"><use href="#i-target"/></svg></span>Cockroach</div>
</section>

<section>
  <div class="abs cta-band" style="background:radial-gradient(ellipse 400px 200px at 600px 180px,rgba(90,170,40,.6),transparent 70%),linear-gradient(180deg,#3a9a0a,#2f8807)" role="img" aria-label="Green-tinted photo of a pest technician at work"></div>
  <svg class="abs" style="left:0;top:3280px" width="1200" height="50" viewBox="0 0 1200 50"><path d="M0 0 H1200 V6 C900 40 400 48 0 24Z" fill="#fff"/></svg>
  <p class="abs cta-text">The Best Pest Control &nbsp;Termite<br>Inspections and Treatments Company.</p>
  <div class="btn btn-outline" style="left:433px;top:3496px;width:149px;height:35px;font-size:12px">Online Inquiry</div>
  <div class="btn btn-black btn-pill" style="left:605px;top:3496px;width:150px;height:35px;font-size:12px">Contact Us</div>
</section>

<footer class="abs site-footer">
  <div class="abs brand" style="left:58px;top:96px;color:#fff;font-size:18px"><span class="brand-dot"></span>Brightmoor Pest Services</div>
  <div class="abs social" style="left:61px;top:186px" aria-label="Social profile"></div>
  <div class="abs social" style="left:98px;top:186px" aria-label="Social profile"></div>
  <div class="abs social" style="left:135px;top:186px" aria-label="Social profile"></div>

  <h3 class="abs foot-title" style="left:337px;top:59px">Site Map</h3>
  <div class="abs foot-link" style="left:341px;top:108px">- Home</div>
  <div class="abs foot-link" style="left:341px;top:142px">- Services</div>
  <div class="abs foot-link" style="left:341px;top:175px">- About Us</div>
  <div class="abs foot-link" style="left:341px;top:209px">- Contact Us</div>

  <h3 class="abs foot-title" style="left:613px;top:59px">Contact Us</h3>
  <svg class="abs" style="left:612px;top:117px" width="16" height="20" viewBox="0 0 16 20"><path d="M8 1a6 6 0 0 0-6 6c0 4.5 6 12 6 12s6-7.5 6-12a6 6 0 0 0-6-6z" fill="none" stroke="#3a9a0a" stroke-width="1.8"/><circle cx="8" cy="7" r="2.2" fill="#3a9a0a"/></svg>
  <div class="abs foot-link" style="left:645px;top:114px;width:200px;line-height:19px">101 - Lorem ipsum is dummy printing text</div>
  <svg class="abs" style="left:611px;top:172px" width="18" height="18" viewBox="0 0 24 24"><path d="M6.6 10.8c1.4 2.8 3.8 5.1 6.6 6.6l2.2-2.2c.3-.3.7-.4 1-.2 1.1.4 2.3.6 3.6.6.6 0 1 .4 1 1V20c0 .6-.4 1-1 1C10.6 21 3 13.4 3 4c0-.6.4-1 1-1h3.5c.6 0 1 .4 1 1 0 1.3.2 2.5.6 3.6.1.3 0 .7-.2 1z" fill="#3a9a0a"/></svg>
  <div class="abs foot-link" style="left:645px;top:172px">02 5550 0137</div>
  <svg class="abs" style="left:612px;top:226px" width="20" height="14" viewBox="0 0 20 14"><rect x="1" y="1" width="18" height="12" fill="none" stroke="#3a9a0a" stroke-width="1.8"/><path d="M1 1 10 8 19 1" fill="none" stroke="#3a9a0a" stroke-width="1.8"/></svg>
  <div class="abs foot-link" style="left:645px;top:224px">info@brightmoorpest.com.au</div>

  <h3 class="abs foot-title" style="left:889px;top:59px">News Letter</h3>
  <div class="abs" style="left:889px;top:110px;width:251px;height:36px;background:#fff;border-radius:18px;font-size:11px;color:#888;padding:11px 10px">Enter Email Addeess..</div>
  <div class="btn btn-green" style="left:889px;top:162px;width:118px;height:35px;border-radius:18px;font-size:12px">Send Now</div>
</footer>

<div class="abs copyright">Copyright © 2021 Brightmoor Pest Services - All Rights Reserved</div>

</body>
</html>
```